Chinese Herbal and Roots Shop design

Hello Designers,

We are a herbal startup company which sells Chinese Herbal Products. we are looking for a responsive and unqiue Ecommerce web design.
Our business name is velorin and our area of business cut across the entire United States.

We don't have a logo at the moment and designers who come up with a great logo is more likely to be awarded winner of the consent.

The design needs to be completely custom design and we are not after just a template design. Please be creative and at the same time design have to be professionally looking and easy to navigate.
A theme which suits a herbal products are desired. We are open to different colors excpet RED and PINK.

NAVIGATION
Header -
Home, products, offers, Blog, cart, login/account

Footer -
Please refer to other Ecommerce websites

Page requires:
HOME PAGE
1. slider(Highlist products)
2. FEATURE PRODUCTS
3. Latest products
4. Most selling products
5. Deal of the day
6. Email capture (Newsletter/signup)
7. Social media links
8. Footer

PRODUCT PAGE
All the products will be present here with required details (price, short note and offers if any)

PRODUCT DETAILS PAGE
A well designed detailed page for a particular product covers the details of the price, increment, short description, purchase and other add to cart button. A section with similar products should be listed below aswell.

Industry/Entity Type

It Company

Coding

Coded - Design and coding required

```html
<!DOCTYPE html>
<html lang="en">
<head>
<meta charset="utf-8">
<title>Velorin Herbals</title>
<link href="https://fonts.googleapis.com/css2?family=Cinzel:wght@400;500&family=Lato:ital,wght@0,400;0,700;0,900;1,400&display=swap" rel="stylesheet">
<style>
:root{
  --green:#3f8f2f;
  --green-dark:#256b27;
  --green-soft:#8bae4f;
  --green-btn:#6f9a36;
  --brown:#4a2d14;
  --ink:#222;
  --muted:#666;
  --grey-bg:#efefef;
  --card-grey:#cfcfcf;
  --footer:#2c2c2c;
  --strike:#e8a21c;
  --deal-blue:#2b5fd1;
}
*{box-sizing:border-box;margin:0;padding:0}
html,body{width:1200px;height:3297px;overflow:hidden}
body{position:relative;font-family:'Lato',sans-serif;color:var(--ink);background:#fff}
.abs{position:absolute}
.sec-title{position:absolute;left:0;width:1200px;text-align:center;font-family:'Cinzel',serif;font-size:34px;letter-spacing:1px;color:var(--ink);white-space:nowrap}
.sec-title span{color:var(--green)}
.sec-title::after{content:"";display:block;width:120px;height:2px;background:var(--green);margin:4px auto 0}

/* header */
.site-header{left:0;top:0;width:1200px;height:88px;background:#fff;border-bottom:3px solid var(--green-dark)}
.account-tab{left:857px;top:0;width:286px;height:22px;background:var(--green-dark);border-radius:0 0 14px 14px;color:#fff;font-size:12px;font-weight:700;display:flex;justify-content:center;gap:40px;align-items:center;letter-spacing:1px;text-transform:uppercase}
.brand{left:99px;top:24px;font-weight:900;font-size:36px;color:var(--green);letter-spacing:-.5px;white-space:nowrap}
.main-nav{left:604px;top:50px;display:flex;align-items:center;font-family:'Cinzel',serif;font-size:16px;font-weight:500;white-space:nowrap}
.main-nav a{color:var(--ink);text-decoration:none;padding:0 12px;border-left:1px solid #999;line-height:16px}
.main-nav a:first-child{border-left:none;padding-left:0;color:var(--green-dark);border-bottom:3px solid var(--green-dark);padding-bottom:6px;margin-bottom:-9px}

/* hero */
.hero{left:0;top:91px;width:1200px;height:711px;overflow:hidden;background:#e9e9e6}
.hero-photo{left:0;top:0;width:1200px;height:711px;background:linear-gradient(160deg,#6f8f3c 0%,#4e6b2a 30%,#7a6a4a 55%,#b9b6a4 80%,#d6d3c5 100%)}
.hero-copy{right:101px;top:142px;text-align:right;color:#fff}
.hero-copy h1{font-size:31px;font-weight:700;line-height:40px;text-shadow:0 1px 3px rgba(0,0,0,.4)}
.hero-copy p{font-size:15px;line-height:20px;margin-top:10px;text-shadow:0 1px 2px rgba(0,0,0,.4)}
.bubble{border-radius:50%;border:8px solid var(--green);box-shadow:0 2px 8px rgba(0,0,0,.3)}
.hero-btn{left:750px;top:628px;width:349px;height:44px;background:var(--green-soft);color:#fff;font-size:15px;display:flex;align-items:center;padding-left:22px;border-radius:2px;white-space:nowrap}
.hero-btn i{position:absolute;right:0;top:0;width:46px;height:44px;background:var(--green-dark);display:flex;align-items:center;justify-content:center;font-style:normal;font-size:24px}

/* latest */
.latest{left:0;top:802px;width:1200px;height:451px;background:#fff;border-bottom:2px solid #7aa58a}
.latest-card{top:128px;width:314px;height:272px;background:#e2e2e2;border:6px solid #d6d6d6;box-shadow:0 6px 8px rgba(0,0,0,.12)}
.latest-card .thumb{width:302px;height:196px;background:#fff}
.latest-card .bar{height:64px;display:flex;align-items:center;padding:0 8px 0 6px;color:var(--green);font-size:21px}
.latest-card .bar .price{flex:1}
.latest-card .bar svg{margin-left:14px}
.slide-arrow{top:236px}

/* deal */
.deal{left:0;top:1253px;width:1200px;height:494px;background:var(--grey-bg);border-bottom:2px solid #7aa58a}
.deal-card{top:110px;width:300px;height:330px;background:#fff}
.deal-card .thumb{margin:13px 12px 0;height:190px}
.deal-card h3{font-weight:400;font-size:21px;margin:14px 0 0 8px}
.deal-card .price{font-size:21px;margin:10px 0 0 8px;color:var(--green)}
.deal-card .price s{color:var(--strike);margin-right:6px}
.deal-btn{position:absolute;left:0;bottom:0;width:300px;height:48px;border:2px solid #555;border-radius:6px;background:#fff;display:flex;align-items:center;padding-left:18px;gap:30px;color:var(--deal-blue);font-size:22px}

/* most selling */
.selling{left:0;top:1747px;width:1200px;height:425px;background:#f5f6f0}
.sell-img{top:126px;width:257px;height:255px;border:2px solid var(--green);background:#fff;padding:8px}
.sell-img div{width:100%;height:100%}
.sell-info{top:128px;width:200px}
.sell-info h4{font-weight:400;font-size:21px}
.sell-info .price{color:var(--green);font-size:21px;margin-top:12px}
.sell-info p{font-size:13px;line-height:25px;color:var(--muted);margin-top:10px}
.buy-btn{display:inline-block;margin-top:15px;background:var(--green-soft);color:#fff;font-size:15px;padding:12px 22px}

/* testimonials */
.testi{left:0;top:2172px;width:1200px;height:345px;background:linear-gradient(90deg,#b9d49a 0%,#e4ecd6 25%,#f4f3ee 55%,#d8cfc0 80%,#a99478 100%)}
.avatar{left:103px;top:119px;width:124px;height:124px;border-radius:50%;border:5px solid #fff;background:linear-gradient(#e6c9a5,#c79a6f);box-shadow:0 2px 6px rgba(0,0,0,.25)}
.quote{left:259px;top:130px;width:840px;font-size:13px;line-height:20px;font-style:italic;color:#333}
.quote-mark{font-family:Georgia,serif;font-size:44px;font-weight:700;color:#222;line-height:1}
.author{left:250px;top:264px;font-size:13px;font-weight:700;color:#222}
.pager{left:1013px;top:326px;display:flex;gap:3px}
.pager i{width:26px;height:14px;background:#c9c9c9;display:block}

/* newsletter */
.news{left:0;top:2517px;width:1200px;height:186px;background:var(--grey-bg)}
.news-box{left:99px;top:43px;width:1000px;height:100px;border:2px solid #ddd;background:#f7f7f7;display:flex;align-items:center}
.news-box h2{font-family:'Cinzel',serif;font-weight:400;font-size:32px;margin-left:20px;white-space:nowrap}
.news-box h2 span{color:var(--green)}
.news-input{left:466px;top:31px;width:328px;height:38px;background:#fff;border:1px solid #ddd;font-size:12px;color:#666;padding:12px 10px}
.news-btn{left:818px;top:31px;width:162px;height:38px;background:var(--green-soft);color:#fff;font-size:17px;display:flex;align-items:center;justify-content:center}

/* footer */
.wave{left:0;top:2703px;width:1200px;height:160px}
.site-footer{left:0;top:2857px;width:1200px;height:330px;background:var(--footer);color:#ddd}
.foot-h{font-family:'Cinzel',serif;font-size:17px;color:#ddd;letter-spacing:1px;white-space:nowrap}
.foot-h::after{content:"";display:block;width:200px;height:1px;background:var(--green);margin-top:6px}
.quick{left:99px;top:48px;width:210px}
.quick ul{list-style:none;margin-top:20px;width:112px}
.quick li{font-size:12px;padding:10px 0 11px 12px;border-bottom:1px dashed #666;position:relative}
.quick li::before{content:"";position:absolute;left:0;top:15px;border-left:5px solid var(--green);border-top:3px solid transparent;border-bottom:3px solid transparent}
.contact{left:396px;top:48px;width:290px}
.contact .row{display:flex;gap:18px;font-size:12px;line-height:18px;padding:10px 0;border-bottom:1px dashed #666}
.contact svg{flex:none;margin-top:2px}
.location{left:807px;top:48px}
.map{margin-top:26px;width:288px;height:206px;background:linear-gradient(135deg,#7e7a5c,#9c9476 40%,#6d7658 70%,#8a8468)}
.ground{left:0;top:3187px;width:1200px;height:110px;background:linear-gradient(#4c8a2a 0%,#3a6e22 35%,#5a3a1c 70%,#3a2410 100%)}
.pay{left:99px;top:77px;display:flex;gap:10px;font-size:11px;font-weight:700;color:#fff}
.pay span{background:rgba(0,0,0,.35);padding:3px 6px;border-radius:3px}
.copyright{left:0;width:1200px;top:79px;text-align:center;font-size:12px;color:#fff}
.social{left:1020px;top:76px;display:flex;gap:10px}
.social i{display:block;width:20px;height:20px;border-radius:50%}
</style>
</head>
<body>

<header class="site-header abs">
  <div class="account-tab abs"><span>&#9662; Cart</span><span>My Account</span></div>
  <div class="brand abs">VELORINHERBALS</div>
  <nav class="main-nav abs">
    <a href="#">Home</a><a href="#">Products &#9662;</a><a href="#">Offers</a><a href="#">Blog</a><a href="#">Contact Us</a>
  </nav>
</header>

<section class="hero abs">
  <div class="hero-photo abs" role="img" aria-label="Cup of herbal tea on a wooden table with dandelion flowers"></div>
  <svg class="abs" style="left:0;top:0" width="1200" height="711" viewBox="0 0 1200 711">
    <path d="M0 470 C 200 640 520 680 760 590 C 950 520 1080 470 1200 470 L1200 711 L0 711Z" fill="#e9e9e6"/>
    <path d="M0 455 C 200 625 520 665 760 575 C 950 505 1080 455 1200 455" fill="none" stroke="#3f8f2f" stroke-width="16"/>
    <path d="M760 600 C 950 530 1080 490 1200 492" fill="none" stroke="#4a2d14" stroke-width="14"/>
  </svg>
  <div class="hero-copy abs">
    <h1>You Can Get All<br>Herbal &amp; Roots Product</h1>
    <p>Lorem ipsum dolor sit amet, consectetuer adipiscing elit,<br>sed diam nonummy nibh euismod tincidunt.</p>
  </div>
  <div class="bubble abs" style="left:330px;top:469px;width:198px;height:198px;background:linear-gradient(#c8b89a,#8c7a5a)" role="img" aria-label="Packets of dried herbal tea"></div>
  <div class="bubble abs" style="left:516px;top:381px;width:220px;height:220px;background:linear-gradient(#8fb06a,#3f6a2a)" role="img" aria-label="Jars of herbal products"></div>
  <div class="bubble abs" style="left:769px;top:294px;width:198px;height:198px;background:linear-gradient(#f4f4f2,#b8d6a8)" role="img" aria-label="Herbal lotion bottles"></div>
  <div class="hero-btn abs">View All Our Featured Products<i>&raquo;</i></div>
</section>

<section class="latest abs">
  <h2 class="sec-title" style="top:40px">Latest <span>Products</span></h2>
  <svg class="slide-arrow abs" style="left:40px" width="30" height="50" viewBox="0 0 30 50"><path d="M26 4 L6 25 L26 46" fill="none" stroke="#aaa" stroke-width="5"/></svg>
  <svg class="slide-arrow abs" style="left:1122px" width="30" height="50" viewBox="0 0 30 50"><path d="M4 4 L24 25 L4 46" fill="none" stroke="#aaa" stroke-width="5"/></svg>
  <div class="latest-card abs" style="left:99px">
    <div class="thumb" role="img" aria-label="Row of herbal drink bottles" style="background:linear-gradient(#fff,#e8dc7a 60%,#fff)"></div>
    <div class="bar"><span class="price">CNY. 500</span>
      <svg width="30" height="26" viewBox="0 0 30 26"><path d="M1 2h5l4 15h15l3-10H8" fill="none" stroke="#3f8f2f" stroke-width="2.5"/><circle cx="12" cy="22" r="2.5" fill="#3f8f2f"/><circle cx="23" cy="22" r="2.5" fill="#3f8f2f"/></svg>
      <svg width="24" height="22" viewBox="0 0 24 22"><path d="M12 21 L2 11 A5.5 5.5 0 0 1 12 4 A5.5 5.5 0 0 1 22 11Z" fill="#d0112b"/></svg>
    </div>
  </div>
  <div class="latest-card abs" style="left:442px">
    <div class="thumb" role="img" aria-label="Jar of herbal paste" style="background:radial-gradient(circle at 50% 50%,#1c2a3a 0 18%,#fff 19%)"></div>
    <div class="bar"><span class="price">CNY. 500</span>
      <svg width="30" height="26" viewBox="0 0 30 26"><path d="M1 2h5l4 15h15l3-10H8" fill="none" stroke="#3f8f2f" stroke-width="2.5"/><circle cx="12" cy="22" r="2.5" fill="#3f8f2f"/><circle cx="23" cy="22" r="2.5" fill="#3f8f2f"/></svg>
      <svg width="24" height="22" viewBox="0 0 24 22"><path d="M12 21 L2 11 A5.5 5.5 0 0 1 12 4 A5.5 5.5 0 0 1 22 11Z" fill="#111"/></svg>
    </div>
  </div>
  <div class="latest-card abs" style="left:785px">
    <div class="thumb" role="img" aria-label="Three supplement bottles" style="background:linear-gradient(90deg,#fff 10%,#8bbf5a 25%,#e8b24a 50%,#a8c070 75%,#fff 90%)"></div>
    <div class="bar"><span class="price">CNY. 500</span>
      <svg width="30" height="26" viewBox="0 0 30 26"><path d="M1 2h5l4 15h15l3-10H8" fill="none" stroke="#3f8f2f" stroke-width="2.5"/><circle cx="12" cy="22" r="2.5" fill="#3f8f2f"/><circle cx="23" cy="22" r="2.5" fill="#3f8f2f"/></svg>
      <svg width="24" height="22" viewBox="0 0 24 22"><path d="M12 21 L2 11 A5.5 5.5 0 0 1 12 4 A5.5 5.5 0 0 1 22 11Z" fill="#111"/></svg>
    </div>
  </div>
</section>

<section class="deal abs">
  <h2 class="sec-title" style="top:42px">Deal Of the <span>Day</span></h2>
  <div class="deal-card abs" style="left:99px">
    <div class="thumb" role="img" aria-label="Boxes of fruit herbal tea" style="background:linear-gradient(135deg,#eee,#b9b0c8 40%,#8a2a50 60%,#ddd)"></div>
    <h3>Lorem Epsom</h3><div class="price"><s>CNY. 500</s> CNY. 350</div>
    <div class="deal-btn"><svg width="34" height="28" viewBox="0 0 30 26"><path d="M1 2h5l4 15h15l3-10H8" fill="none" stroke="#3f8f2f" stroke-width="2.5"/><circle cx="12" cy="22" r="2.5" fill="#3f8f2f"/><circle cx="23" cy="22" r="2.5" fill="#3f8f2f"/></svg>GET DEAL</div>
  </div>
  <div class="deal-card abs" style="left:451px">
    <div class="thumb" role="img" aria-label="Coconut with organic product pouch" style="background:linear-gradient(135deg,#f6f6f0,#d9e8c0 45%,#e8e8e8)"></div>
    <h3>Lorem Epsom</h3><div class="price"><s>CNY. 400</s> CNY. 250</div>
    <div class="deal-btn"><svg width="34" height="28" viewBox="0 0 30 26"><path d="M1 2h5l4 15h15l3-10H8" fill="none" stroke="#3f8f2f" stroke-width="2.5"/><circle cx="12" cy="22" r="2.5" fill="#3f8f2f"/><circle cx="23" cy="22" r="2.5" fill="#3f8f2f"/></svg>GET DEAL</div>
  </div>
  <div class="deal-card abs" style="left:799px">
    <div class="thumb" role="img" aria-label="Three dark supplement jars" style="background:linear-gradient(#fff,#2a2a22 45%,#6a5a2a 70%,#fff)"></div>
    <h3>Lorem Epsom</h3><div class="price"><s>CNY. 700</s> CNY. 550</div>
    <div class="deal-btn"><svg width="34" height="28" viewBox="0 0 30 26"><path d="M1 2h5l4 15h15l3-10H8" fill="none" stroke="#3f8f2f" stroke-width="2.5"/><circle cx="12" cy="22" r="2.5" fill="#3f8f2f"/><circle cx="23" cy="22" r="2.5" fill="#3f8f2f"/></svg>GET DEAL</div>
  </div>
</section>

<section class="selling abs">
  <h2 class="sec-title" style="top:48px">Most Selling <span>Products</span></h2>
  <div class="sell-img abs" style="left:99px"><div role="img" aria-label="Bottle of herbal oil" style="background:linear-gradient(90deg,#fff 35%,#c8683a 45%,#a84a22 55%,#fff 65%)"></div></div>
  <div class="sell-info abs" style="left:380px">
    <h4>Herbal</h4><div class="price">CNY 110.00</div>
    <p>Lorem ipsum dolor sit amet, consectetuer adipiscing elit, sed diam nonummy nibh euismod tincidunt ut laoreet dolore magna aliquam erat volutpat.</p>
    <span class="buy-btn">BUY NOW</span>
  </div>
  <div class="sell-img abs" style="left:600px"><div role="img" aria-label="Herbal cream box and tube" style="background:linear-gradient(135deg,#fff,#e9e36a 40%,#3f8f2f 60%,#fff)"></div></div>
  <div class="sell-info abs" style="left:879px">
    <h4>Herbal</h4><div class="price">CNY 110.00</div>
    <p>Lorem ipsum dolor sit amet, consectetuer adipiscing elit, sed diam nonummy nibh euismod tincidunt ut laoreet dolore magna aliquam erat volutpat.</p>
    <span class="buy-btn">BUY NOW</span>
  </div>
</section>

<section class="testi abs" role="img" aria-label="Soft background of green leaves and dried herbs">
  <h2 class="sec-title" style="top:40px">Client <span>Testimonials</span></h2>
  <div class="avatar abs" role="img" aria-label="Customer portrait"></div>
  <div class="quote abs"><span class="quote-mark">&ldquo;</span> Lorem ipsum dolor sit amet, consectetuer adipiscing elit, sed diam nonummy nibh euismod tincidunt ut laoreet dolore magna aliquam erat volutpat. Ut wisi enim ad minim veniam, quis nostrud exerci tation ullamcorper suscipit lobortis nisl ut aliquip ex ea commodo consequat. Duis autem vel eum iriure dolor in hendrerit in vulputate velit esse molestie consequat, vel illum dolore eu feugiat nulla facilisis at vero eros et accumsan et iusto odio dignissim qui blandit praesent luptatum zzril delenit augue duis dolore te feugait nulla facilisi. vel illum dolore eu feugiat nulla facilisis at vero eros et accumsan et iusto odio dignissim qui blandit praesent luptatum zzril delenit augue.<span class="quote-mark" style="float:right;margin-right:40px">&rdquo;</span></div>
  <div class="author abs">- sollicitudin nunc</div>
  <div class="pager abs"><i></i><i></i><i></i></div>
</section>

<section class="news abs">
  <div class="news-box abs">
    <svg style="margin-left:20px" width="52" height="52" viewBox="0 0 52 52"><circle cx="26" cy="26" r="24" fill="none" stroke="#256b27" stroke-width="3"/><rect x="13" y="17" width="26" height="18" fill="#256b27"/><path d="M13 17 L26 28 L39 17" fill="none" stroke="#fff" stroke-width="2"/></svg>
    <h2>Newsletter <span>Signup</span></h2>
    <div class="news-input abs">Enter your email here</div>
    <div class="news-btn abs">Subscribe</div>
  </div>
</section>

<svg class="wave abs" viewBox="0 0 1200 160" width="1200" height="160">
  <rect width="1200" height="160" fill="#efefef"/>
  <path d="M0 100 C 250 150 500 140 760 70 C 940 20 1080 10 1200 20 L1200 160 L0 160Z" fill="#2c2c2c"/>
  <path d="M0 88 C 250 140 500 128 760 58 C 940 8 1080 0 1200 8" fill="none" stroke="#4a2d14" stroke-width="14"/>
  <path d="M0 60 C 120 110 260 130 380 125 C 200 120 80 95 0 75Z" fill="#3f8f2f"/>
  <path d="M760 40 C 940 -5 1080 -10 1200 0 L1200 10 C 1080 2 940 10 760 48Z" fill="#3f8f2f"/>
</svg>

<footer class="site-footer abs">
  <div class="quick abs">
    <div class="foot-h">Quick Links</div>
    <ul><li>Home</li><li>Products</li><li>Offers</li><li>Blog</li><li>Contact Us</li></ul>
  </div>
  <div class="contact abs">
    <div class="foot-h">Contact Info</div>
    <div style="margin-top:20px">
      <div class="row"><svg width="14" height="18" viewBox="0 0 14 18"><path d="M7 17 C2 10 1 8 1 6 A6 6 0 0 1 13 6 C13 8 12 10 7 17Z" fill="#3f8f2f"/><circle cx="7" cy="6" r="2" fill="#2c2c2c"/></svg><span>Velorinherbals<br>1234, Lorem Epsom</span></div>
      <div class="row"><svg width="16" height="16" viewBox="0 0 16 16"><path d="M3 1 L6 1 L7 5 L5 6 C6 9 7 10 10 11 L11 9 L15 10 L15 13 C15 14 14 15 13 15 C6 15 1 10 1 3 C1 2 2 1 3 1Z" fill="#3f8f2f"/></svg><span>123-456-7890</span></div>
      <div class="row"><svg width="16" height="16" viewBox="0 0 16 16"><path d="M3 1 L6 1 L7 5 L5 6 C6 9 7 10 10 11 L11 9 L15 10 L15 13 C15 14 14 15 13 15 C6 15 1 10 1 3 C1 2 2 1 3 1Z" fill="#3f8f2f"/></svg><span>123-456-7890</span></div>
      <div class="row"><svg width="18" height="14" viewBox="0 0 18 14"><rect width="18" height="14" rx="2" fill="#3f8f2f"/><path d="M1 1 L9 8 L17 1" fill="none" stroke="#2c2c2c" stroke-width="1.5"/></svg><span>info@velorinherbals.com</span></div>
    </div>
  </div>
  <div class="location abs">
    <div class="foot-h">Our Location</div>
    <div class="map" role="img" aria-label="Map showing the shop location"></div>
  </div>
</footer>

<div class="ground abs" role="img" aria-label="Grass and soil strip">
  <div class="pay abs"><span>Orbicard</span><span>Vantacard</span><span>Paywell</span><span>Maxpay</span></div>
  <div class="copyright abs">&copy; 2017 VELORINHERBALS. All Rights Reserved</div>
  <div class="social abs" aria-label="Social media links"><i style="background:#e8a21c"></i><i style="background:#3aa0d8"></i><i style="background:#6ab04c"></i></div>
</div>

</body>
</html>
```